Postcard Design

R.K Landscaping 484-883-7758Mulching Mowing Planting Spring and Fall Clean up

The colors I would like to work with Are black and green.I do have a Facebook page it's https://www.example-social.test/RK-Landscaping-904417362018834/

For my business logo I would like to put that either on the corner or in the background

Services: mowing, mulching, fall and spring cleanup, hedge trimming

Industry/Entity Type

Landscaping

Requirements
Must have
• Please use these pics
• I like Design #9926064
• and room for addresses to
Should not have
• the pics in the back of card

```html
<!DOCTYPE html>
<html lang="en">
<head>
<meta charset="utf-8">
<title>R.K Landscaping Postcard</title>
<link href="https://fonts.googleapis.com/css2?family=Oswald:wght@600&family=Open+Sans:wght@600;700&family=Libre+Baskerville:ital,wght@1,700&display=swap" rel="stylesheet">
<style>
  :root {
    --stage: #e6e7e8;
    --black: #0b0b0b;
    --white: #ffffff;
    --green: #17964a;
    --siding-dark: #3c3f42;
    --siding-light: #6d7075;
    --lawn: #4f8a2c;
    --lawn-dark: #2f5a1c;
    --sky: #8fbbe6;
  }
  * { margin: 0; padding: 0; box-sizing: border-box; }
  html, body {
    width: 1200px; height: 978px; overflow: hidden;
    background: var(--stage);
  }
  .postcard {
    position: absolute;
    left: 135px; top: 120px;
    width: 932px; height: 723px;
    overflow: hidden;
    background: var(--black);
  }
  .postcard__art {
    position: absolute; inset: 0;
    width: 932px; height: 723px;
  }
  .brand {
    position: absolute;
    left: 20px; top: 40px;
    width: 340px;
    text-align: center;
    color: var(--black);
  }
  .brand__mark {
    width: 110px; height: 110px;
    margin: 0 auto 22px;
    border-radius: 50%;
    background: var(--black);
  }
  .brand__name {
    font-family: "Oswald", sans-serif;
    font-weight: 600;
    font-size: 44px;
    line-height: 1.05;
    letter-spacing: 0.5px;
    text-transform: uppercase;
  }
  .brand__tagline {
    margin-top: 12px;
    font-family: "Libre Baskerville", serif;
    font-style: italic;
    font-weight: 700;
    font-size: 18px;
    line-height: 1.2;
  }
  .brand__phone {
    margin-top: 16px;
    font-family: "Open Sans", sans-serif;
    font-weight: 700;
    font-size: 29px;
    letter-spacing: 1px;
  }
  .services {
    position: absolute;
    left: 496px; top: 40px;
    list-style: none;
    font-family: "Open Sans", sans-serif;
    font-weight: 600;
    font-size: 22px;
    color: var(--white);
  }
  .services__item {
    display: flex; align-items: center;
    height: 40px;
  }
  .services__item::before {
    content: "";
    width: 12px; height: 12px;
    margin-right: 14px;
    border-radius: 50%;
    background: var(--green);
  }
</style>
</head>
<body>
  <div class="postcard">
    <svg class="postcard__art" viewBox="0 0 932 723" xmlns="http://www.w3.org/2000/svg">
      <defs>
        <linearGradient id="sidingTone" x1="0" y1="0" x2="1" y2="1">
          <stop offset="0" stop-color="var(--siding-light)"/>
          <stop offset="1" stop-color="var(--siding-dark)"/>
        </linearGradient>
        <linearGradient id="yardTone" x1="0" y1="0" x2="0" y2="1">
          <stop offset="0" stop-color="var(--sky)"/>
          <stop offset="0.35" stop-color="#7d8f76"/>
          <stop offset="0.55" stop-color="var(--lawn-dark)"/>
          <stop offset="1" stop-color="var(--lawn)"/>
        </linearGradient>
      </defs>

      <rect class="photo-porch" x="300" y="0" width="632" height="400" fill="url(#sidingTone)"
            role="img" aria-label="Photo of a house porch with grey siding and a mulched bed"/>
      <rect x="300" y="0" width="632" height="400" fill="#000" opacity="0.35"/>

      <path class="band band--yard" d="M932,204 C700,198 420,252 290,405 C215,495 165,610 148,723 L932,723 Z" fill="var(--green)"/>
      <path class="photo-yard" d="M932,222 C700,215 420,270 305,420 C232,510 182,620 166,723 L932,723 Z"
            fill="url(#yardTone)" role="img" aria-label="Photo of a freshly mowed backyard lawn behind a two-storey house with a deck"/>

      <path class="band band--brand" d="M0,0 L370,0 C412,100 408,270 318,398 C245,492 130,545 0,550 Z" fill="var(--green)"/>
      <path class="panel-brand" d="M0,0 L340,0 C380,90 390,250 300,380 C230,470 120,530 0,531 Z" fill="var(--white)"/>
    </svg>

    <div class="brand">
      <div class="brand__mark"></div>
      <div class="brand__name">R.K Landscaping</div>
      <p class="brand__tagline">For all your Professional<br>Landscaping Needs</p>
      <p class="brand__phone">555-216-0493</p>
    </div>

    <ul class="services">
      <li class="services__item">MOWING</li>
      <li class="services__item">MULCHING</li>
      <li class="services__item">FALL AND SPRING CLEANUP</li>
      <li class="services__item">HEDGE TRIMMING</li>
    </ul>
  </div>
</body>
</html>
```